Brinevale Yacht Management Full Page Ad Flyer

Yacht Management Package also includes the following periodic Monthly services:

Monthly full vessel systems checklist inspections
Diver For Hull Cleaning And Inspection Of Props, Shafts, and Zincs
Interior/Exterior Detailing and scheduled washdowns
Manage Haulout
Pump-out Services
On-call Captain and Crew Services
Updates

Need more time to provide more content to designers and the printing press template file.

Target Market(s)

Vessel owners, motor yachts, sailboats from 25 feet in length up to 125 feet in length. We do not do cruise ships or yachts larger than 125 feet. Someone who has their boat docked at their house or a local marina. We also offer mobile on-site services.

```html
<!DOCTYPE html>
<html lang="en">
<head>
<meta charset="utf-8">
<title>Brinevale Yacht Management – Periodic Monthly Services</title>
<link href="https://fonts.googleapis.com/css2?family=Michroma&family=Poppins:wght@300;400;600;700;800&display=swap" rel="stylesheet">
<style>
  :root {
    --sea-deep: #0c4660;
    --sea-mid: #0d5668;
    --sea-low: #0b4f5e;
    --title-blue: #1c73a0;
    --cyan: #10d0ea;
    --white: #ffffff;
    --panel: rgba(28, 150, 160, 0.42);
    --divider: rgba(255, 255, 255, 0.75);
    --badge-red: #8a1d2e;
  }
  * { box-sizing: border-box; margin: 0; padding: 0; }
  html, body { width: 962px; height: 1200px; overflow: hidden; background: #e4dcdd; }
  .flyer {
    position: relative;
    width: 962px;
    height: 1200px;
    overflow: hidden;
    font-family: "Poppins", Arial, sans-serif;
    color: var(--white);
  }
  .sea-photo {
    position: absolute; inset: 0;
    background:
      radial-gradient(ellipse at 70% 55%, rgba(20, 110, 120, 0.55), transparent 60%),
      linear-gradient(170deg, var(--sea-deep) 0%, var(--sea-mid) 55%, var(--sea-low) 100%);
  }
  .yacht-photo {
    position: absolute;
    left: 388px; top: 316px;
    width: 574px; height: 562px;
    background: radial-gradient(ellipse 62% 26% at 55% 48%, rgba(240, 242, 246, 0.92) 0%, rgba(214, 220, 228, 0.7) 55%, rgba(214, 220, 228, 0) 100%);
    transform: rotate(35deg);
    transform-origin: 50% 50%;
  }
  .headline { position: absolute; left: 74px; top: 58px; }
  .headline-brand {
    font-family: "Michroma", Arial, sans-serif;
    color: var(--title-blue);
    font-size: 64px;
    line-height: 62px;
    letter-spacing: -1px;
  }
  .headline-accent, .headline-main {
    font-family: "Poppins", Arial, sans-serif;
    font-weight: 700;
    font-size: 62px;
    line-height: 58px;
    letter-spacing: -1.5px;
  }
  .headline-accent { color: var(--cyan); margin-top: 8px; }
  .headline-main { color: var(--white); }
  .service-panel {
    position: absolute;
    left: 67px; top: 339px;
    width: 469px; height: 651px;
    background: var(--panel);
    border-radius: 20px;
    padding: 28px 0 0 29px;
  }
  .service-list { list-style: none; width: 360px; }
  .service-item {
    display: flex; gap: 12px;
    font-size: 23.5px;
    line-height: 27px;
    padding: 12px 0 14px;
    border-bottom: 1.5px dashed var(--divider);
  }
  .service-item:last-child { border-bottom: none; }
  .service-item span { white-space: nowrap; }
  .tick { flex: none; width: 20px; height: 20px; margin-top: 4px; }
  .offer-badge { position: absolute; left: 576px; top: 318px; width: 230px; height: 230px; }
  .offer-text {
    position: absolute; left: 576px; top: 374px; width: 230px;
    text-align: center; font-weight: 700;
  }
  .offer-kicker { font-size: 12.5px; font-weight: 400; letter-spacing: 2px; line-height: 16px; }
  .offer-big { color: var(--cyan); font-size: 36px; line-height: 36px; letter-spacing: -0.5px; }
  .offer-sub { font-size: 22px; line-height: 26px; }
  .contact { position: absolute; left: 562px; top: 884px; width: 340px; }
  .contact-kicker { font-size: 17px; font-weight: 300; letter-spacing: 5.5px; line-height: 24px; }
  .contact-offer { color: var(--cyan); font-size: 25px; font-weight: 700; letter-spacing: 6px; line-height: 32px; }
  .contact-phone { display: flex; align-items: center; gap: 6px; font-size: 33px; font-weight: 700; line-height: 44px; }
  .contact-phone svg { width: 26px; height: 26px; }
  .contact-rule { border-top: 1.5px dashed var(--divider); margin: 12px 0 6px; width: 335px; }
  .location-kicker { display: flex; align-items: center; gap: 8px; font-size: 18px; font-weight: 300; letter-spacing: 5px; line-height: 30px; }
  .location-kicker svg { width: 16px; height: 20px; }
  .location-name { color: var(--cyan); font-size: 33px; font-weight: 700; line-height: 38px; letter-spacing: -0.5px; margin-top: 4px; }
  .brand-name {
    position: absolute; left: 67px; top: 1062px; width: 380px;
    text-align: center; font-weight: 400; font-size: 24px; line-height: 32px; letter-spacing: 7px;
    color: var(--white);
  }
</style>
</head>
<body>
<main class="flyer">
  <div class="sea-photo" role="img" aria-label="Aerial photo of deep teal open sea"></div>
  <div class="yacht-photo" role="img" aria-label="Aerial photo of a white motor yacht with tender cruising diagonally"></div>

  <header class="headline">
    <h1 class="headline-brand">YACHT<br>MANAGEMENT</h1>
    <p class="headline-accent">PERIODIC MONTHLY</p>
    <p class="headline-main">SERVICES</p>
  </header>

  <section class="service-panel">
    <ul class="service-list">
      <li class="service-item"><svg class="tick" viewBox="0 0 20 20"><circle cx="10" cy="10" r="10" fill="#10d0ea"/><path d="M5.5 10.2l3 3 6-6" fill="none" stroke="#0d5668" stroke-width="2.2" stroke-linecap="round" stroke-linejoin="round"/></svg><span>Monthly full<br>vessel systems<br>checklist inspections</span></li>
      <li class="service-item"><svg class="tick" viewBox="0 0 20 20"><circle cx="10" cy="10" r="10" fill="#10d0ea"/><path d="M5.5 10.2l3 3 6-6" fill="none" stroke="#0d5668" stroke-width="2.2" stroke-linecap="round" stroke-linejoin="round"/></svg><span>Diver For Hull Cleaning<br>&amp; Inspection Of Props,<br>Shafts, &amp; Zincs</span></li>
      <li class="service-item"><svg class="tick" viewBox="0 0 20 20"><circle cx="10" cy="10" r="10" fill="#10d0ea"/><path d="M5.5 10.2l3 3 6-6" fill="none" stroke="#0d5668" stroke-width="2.2" stroke-linecap="round" stroke-linejoin="round"/></svg><span>Interior/Exterior Detailing<br>&amp; scheduled washdowns</span></li>
      <li class="service-item"><svg class="tick" viewBox="0 0 20 20"><circle cx="10" cy="10" r="10" fill="#10d0ea"/><path d="M5.5 10.2l3 3 6-6" fill="none" stroke="#0d5668" stroke-width="2.2" stroke-linecap="round" stroke-linejoin="round"/></svg><span>Manage Haulout</span></li>
      <li class="service-item"><svg class="tick" viewBox="0 0 20 20"><circle cx="10" cy="10" r="10" fill="#10d0ea"/><path d="M5.5 10.2l3 3 6-6" fill="none" stroke="#0d5668" stroke-width="2.2" stroke-linecap="round" stroke-linejoin="round"/></svg><span>Pump-out Services</span></li>
      <li class="service-item"><svg class="tick" viewBox="0 0 20 20"><circle cx="10" cy="10" r="10" fill="#10d0ea"/><path d="M5.5 10.2l3 3 6-6" fill="none" stroke="#0d5668" stroke-width="2.2" stroke-linecap="round" stroke-linejoin="round"/></svg><span>On-call Captain and<br>Crew Services</span></li>
    </ul>
  </section>

  <svg class="offer-badge" viewBox="-100 -100 200 200" aria-hidden="true">
    <polygon fill="#8a1d2e" points="0,-100 17,-87 34,-94 44,-76 64,-77 66,-57 85,-51 80,-32 97,-21 86,-5 97,12 80,22 86,42 66,47 64,67 44,66 34,85 17,79 0,92 -17,79 -34,85 -44,66 -64,67 -66,47 -86,42 -80,22 -97,12 -86,-5 -97,-21 -80,-32 -85,-51 -66,-57 -64,-77 -44,-76 -34,-94 -17,-87"/>
  </svg>
  <div class="offer-text">
    <p class="offer-kicker">WE ALSO OFFER</p>
    <p class="offer-big">MOBILE<br>ON-SITE</p>
    <p class="offer-sub">SERVICES</p>
  </div>

  <section class="contact">
    <p class="contact-kicker">CALL TODAY FOR A</p>
    <p class="contact-offer">FREE ESTIMATE</p>
    <p class="contact-phone"><svg viewBox="0 0 26 26" aria-hidden="true"><circle cx="13" cy="13" r="13" fill="#10d0ea"/><path d="M9 6.5c.8-.5 1.6-.3 2 .5l1.2 2.4c.3.7.1 1.3-.5 1.7l-.9.6c.6 1.6 1.9 2.9 3.5 3.6l.6-.9c.4-.6 1.1-.8 1.7-.5l2.4 1.2c.8.4 1 1.2.5 2l-.8 1.2c-.6.9-1.7 1.3-2.8 1-4.6-1.3-8-4.7-9.2-9.3-.3-1.1.1-2.2 1-2.8z" fill="#0d5668"/></svg>0255 014 782</p>
    <div class="contact-rule"></div>
    <p class="location-kicker"><svg viewBox="0 0 16 20" aria-hidden="true"><path d="M8 0C3.6 0 0 3.4 0 7.6 0 13 8 20 8 20s8-7 8-12.4C16 3.4 12.4 0 8 0z" fill="#10d0ea"/><circle cx="8" cy="7.6" r="3" fill="#0d5668"/></svg>LOCATED IN</p>
    <p class="location-name">South Florida<br>Miami area</p>
  </section>

  <p class="brand-name">BRINEVALE<br>YACHT MANAGEMENT</p>
</main>
</body>
</html>
```